Service Plan Sales Flyer

The Watchpost Depot (www.kelvarnguard.com) is a commercial security integrator that installs security cameras, access control, intrusion, two-way radios and perimeter security. We require a one page flyer for our service plan for new and existing customers. The price of the service plan is $299/yr and includes the following;
1. Discounted service rate of $118/hr
2. Free remote support ($85/hr without a plan)
3. Free remote training
4. Priority support

Please review our brochure attached and create a one page sales flyer with the end goal of having the client sign up for our annual service plan . The plan will automatically renew every year. Email sales@kelvarnguard.com.

Target Market(s)

commercial industrial clients - no residential

Industry/Entity Type

review our website at www.kelvarnguard.com

Colors
0054AA
0677BA
7BADD7
CADEEF
E8F1F8
EE7325
F08F49
F5BC92
FAE3D3
FDF4ED

Requirements
Must have
• call to action
Should not have
• too many colors

```html
<!DOCTYPE html>
<html lang="en">
<head>
<meta charset="utf-8">
<title>The Watchpost Depot – Service Plan Flyer</title>
<link rel="stylesheet" href="https://fonts.googleapis.com/css2?family=Bebas+Neue&family=Poppins:wght@400;500&display=swap">
<style>
  :root {
    --red: #e8433f;
    --red-deep: #c22d2a;
    --navy: #123462;
    --navy-dark: #0e2a52;
    --paper: #f4f5f7;
    --ink: #1d2a3f;
    --white: #ffffff;
    --stage: #ffffff;
    --rule: #9aa3b0;
  }
  * { margin: 0; padding: 0; box-sizing: border-box; }
  html, body {
    width: 1200px; height: 2400px; overflow: hidden;
    background: var(--stage);
  }
  .flyer {
    position: absolute; left: 40px; top: 476px;
    width: 1120px; height: 1447px;
    background: linear-gradient(180deg, #eef0f3 0%, var(--paper) 40%, #fafafa 100%);
    overflow: hidden;
    font-family: "Poppins", sans-serif;
    color: var(--ink);
  }
  .flyer-shapes { position: absolute; inset: 0; width: 100%; height: 100%; }
  .display { font-family: "Bebas Neue", sans-serif; font-weight: 400; }

  .brand { position: absolute; left: 72px; top: 58px; display: flex; align-items: center; gap: 16px; }
  .brand-mark { width: 52px; height: 52px; background: var(--navy); }
  .brand-name { font-family: "Bebas Neue", sans-serif; font-size: 50px; line-height: 1; color: var(--navy); padding-top: 4px; }

  .headline {
    position: absolute; left: 74px; top: 172px;
    font-size: 88px; line-height: 76px; color: var(--navy);
  }

  .section-title { position: absolute; left: 76px; font-size: 36px; line-height: 1; color: var(--red); }
  .about-title { top: 444px; }
  .products-title { top: 788px; }
  .products-rule { position: absolute; left: 76px; top: 826px; width: 42px; height: 3px; background: var(--rule); }

  .about-copy { position: absolute; left: 76px; width: 445px; font-size: 16px; line-height: 20px; color: var(--ink); }
  .about-copy.first { top: 503px; }
  .about-copy.second { top: 612px; }

  .keypad-photo {
    position: absolute; left: 0; top: 848px; width: 240px; height: 474px;
    background: linear-gradient(90deg, #b9bcc2 0%, #d6d8dc 55%, rgba(244,245,247,0) 100%);
  }

  .product { position: absolute; left: 257px; display: flex; align-items: center; gap: 17px; }
  .product svg { width: 84px; height: 84px; flex: none; }
  .product-label { font-size: 17px; line-height: 20px; color: var(--ink); }

  .price-intro {
    position: absolute; left: 638px; top: 262px;
    font-size: 60px; line-height: 60px; color: var(--white);
  }
  .price-amount {
    position: absolute; left: 634px; top: 388px;
    font-size: 118px; line-height: 1; color: var(--white);
  }

  .equipment-photo {
    position: absolute; left: 642px; top: 584px; width: 432px; height: 278px;
    background: radial-gradient(ellipse at 50% 55%, #dfe4ea 0%, #b7c1ce 45%, rgba(18,52,98,0) 75%);
  }

  .benefits { position: absolute; left: 682px; top: 0; width: 380px; list-style: none; }
  .benefit { position: absolute; left: 0; display: flex; gap: 20px; align-items: flex-start; width: 380px; }
  .benefit svg { width: 28px; height: 28px; flex: none; margin-top: 2px; }
  .benefit-text { font-size: 22px; line-height: 28px; color: var(--white); text-transform: uppercase; letter-spacing: 0.3px; white-space: nowrap; }
  .benefit-rule { position: absolute; left: 726px; width: 318px; border-top: 2px dotted rgba(255,255,255,0.55); }

  .footer {
    position: absolute; left: 0; top: 1321px; width: 100%; height: 126px;
    background: var(--red);
  }
  .footer-phone { position: absolute; left: 72px; top: 28px; display: flex; align-items: center; gap: 16px; }
  .footer-phone svg { width: 38px; height: 38px; }
  .phone-number { font-size: 72px; line-height: 1; color: var(--white); padding-top: 6px; }
  .footer-divider { position: absolute; left: 562px; top: 34px; width: 2px; height: 66px; background: rgba(255,255,255,0.8); }
  .footer-contact { position: absolute; left: 620px; top: 26px; list-style: none; }
  .footer-contact li { display: flex; align-items: center; gap: 18px; height: 36px; font-size: 26px; color: var(--white); }
  .footer-contact svg { width: 28px; height: 28px; flex: none; }
</style>
</head>
<body>
<main class="flyer">
  <svg class="flyer-shapes" viewBox="0 0 767 992" preserveAspectRatio="none" aria-hidden="true">
    <defs>
      <linearGradient id="redPanel" x1="1" y1="0" x2="0" y2="1">
        <stop offset="0" stop-color="#b82825"/>
        <stop offset="1" stop-color="#e8433f"/>
      </linearGradient>
    </defs>
    <polygon points="407,360 767,530 767,905 407,905" fill="#123462"/>
    <polygon points="728,0 767,0 767,530 407,360 282,295 282,205" fill="url(#redPanel)"/>
  </svg>

  <div class="brand">
    <span class="brand-mark"></span>
    <span class="brand-name">The Watchpost Depot</span>
  </div>

  <h1 class="headline display">Knowledgeable<br>Reliable<br>Easy</h1>

  <h2 class="section-title about-title display">About Us</h2>
  <p class="about-copy first">From it's humble beginning in 1999, The Watchpost Depot Employees have worked hard to become one of Canada's most trusted commercial security integrators.</p>
  <p class="about-copy second">We started 20 years ago when businesses still used VCR tapes to record their terrible grainy video for the entire day. Now we are called on by the smartest clients (that's you) to install high definition camera systems, card swipe access control, alarm systems and intercoms ... all accessible on their phones, tablets and PC.</p>

  <h2 class="section-title products-title display">Products</h2>
  <span class="products-rule"></span>

  <div class="keypad-photo" role="img" aria-label="Photo of a hand using a card keypad access reader on a door"></div>

  <div class="product" style="top:848px">
    <svg viewBox="0 0 84 84" aria-hidden="true"><circle cx="42" cy="42" r="39" fill="#fff" stroke="#e8433f" stroke-width="3"/><rect x="26" y="34" width="30" height="16" rx="2" fill="#e8433f"/><polygon points="56,38 64,34 64,50 56,46" fill="#e8433f"/><rect x="36" y="22" width="3" height="12" fill="#e8433f"/><rect x="20" y="54" width="14" height="4" fill="#e8433f"/></svg>
    <span class="product-label">Security Camera<br>System</span>
  </div>
  <div class="product" style="top:958px">
    <svg viewBox="0 0 84 84" aria-hidden="true"><circle cx="42" cy="42" r="39" fill="#fff" stroke="#e8433f" stroke-width="3"/><circle cx="50" cy="34" r="9" fill="none" stroke="#e8433f" stroke-width="4"/><line x1="44" y1="40" x2="26" y2="58" stroke="#e8433f" stroke-width="4"/><line x1="30" y1="54" x2="35" y2="59" stroke="#e8433f" stroke-width="4"/><line x1="18" y1="18" x2="66" y2="66" stroke="#e8433f" stroke-width="3"/></svg>
    <span class="product-label">Access Control<br>&amp; Intercom</span>
  </div>
  <div class="product" style="top:1068px">
    <svg viewBox="0 0 84 84" aria-hidden="true"><circle cx="42" cy="42" r="39" fill="#fff" stroke="#e8433f" stroke-width="3"/><rect x="26" y="22" width="32" height="40" rx="3" fill="none" stroke="#e8433f" stroke-width="3"/><rect x="31" y="27" width="22" height="8" fill="#e8433f"/><g fill="#e8433f"><rect x="31" y="40" width="5" height="5"/><rect x="39.5" y="40" width="5" height="5"/><rect x="48" y="40" width="5" height="5"/><rect x="31" y="49" width="5" height="5"/><rect x="39.5" y="49" width="5" height="5"/><rect x="48" y="49" width="5" height="5"/></g></svg>
    <span class="product-label">Intrusion<br>Alarm</span>
  </div>
  <div class="product" style="top:1180px">
    <svg viewBox="0 0 84 84" aria-hidden="true"><circle cx="42" cy="42" r="39" fill="#fff" stroke="#e8433f" stroke-width="3"/><g stroke="#e8433f" stroke-width="3" fill="none"><line x1="20" y1="36" x2="20" y2="62"/><line x1="30" y1="32" x2="30" y2="62"/><line x1="40" y1="36" x2="40" y2="62"/><line x1="50" y1="40" x2="50" y2="62"/><line x1="16" y1="44" x2="56" y2="44"/><line x1="16" y1="54" x2="56" y2="54"/><path d="M56 26 l10 4 v8 c0 6 -5 9 -10 11 c-5 -2 -10 -5 -10 -11 v-8 z"/></g></svg>
    <span class="product-label">Perimeter<br>Security</span>
  </div>

  <p class="price-intro display">The price of the<br>service plan is</p>
  <p class="price-amount display">$299/YRY</p>

  <div class="equipment-photo" role="img" aria-label="Photo of a door, a monitor showing camera footage, a dome camera and a bullet camera"></div>

  <ul class="benefits">
    <li class="benefit" style="top:930px">
      <svg viewBox="0 0 28 28" aria-hidden="true"><path d="M24 12 A11 11 0 1 1 18 4" fill="none" stroke="#fff" stroke-width="2"/><path d="M8 13 l5 5 l12 -13" fill="none" stroke="#fff" stroke-width="2"/></svg>
      <span class="benefit-text">Discounted service<br>rate of $118/hr</span>
    </li>
    <li class="benefit" style="top:1041px">
      <svg viewBox="0 0 28 28" aria-hidden="true"><path d="M24 12 A11 11 0 1 1 18 4" fill="none" stroke="#fff" stroke-width="2"/><path d="M8 13 l5 5 l12 -13" fill="none" stroke="#fff" stroke-width="2"/></svg>
      <span class="benefit-text">Free remote support<br>($85/hr without a plan)</span>
    </li>
    <li class="benefit" style="top:1163px">
      <svg viewBox="0 0 28 28" aria-hidden="true"><path d="M24 12 A11 11 0 1 1 18 4" fill="none" stroke="#fff" stroke-width="2"/><path d="M8 13 l5 5 l12 -13" fill="none" stroke="#fff" stroke-width="2"/></svg>
      <span class="benefit-text">Free remote training</span>
    </li>
    <li class="benefit" style="top:1240px">
      <svg viewBox="0 0 28 28" aria-hidden="true"><path d="M24 12 A11 11 0 1 1 18 4" fill="none" stroke="#fff" stroke-width="2"/><path d="M8 13 l5 5 l12 -13" fill="none" stroke="#fff" stroke-width="2"/></svg>
      <span class="benefit-text">Priority support</span>
    </li>
  </ul>
  <span class="benefit-rule" style="top:1008px"></span>
  <span class="benefit-rule" style="top:1125px"></span>
  <span class="benefit-rule" style="top:1212px"></span>

  <footer class="footer">
    <div class="footer-phone">
      <svg viewBox="0 0 38 38" aria-hidden="true"><path d="M9 4 l6 7 l-4 5 c2 5 6 9 11 11 l5 -4 l7 6 l-4 6 c-12 -1 -24 -13 -25 -25 z" fill="none" stroke="#fff" stroke-width="2.4" stroke-linejoin="round"/></svg>
      <span class="phone-number display">1-877-555-0142</span>
    </div>
    <span class="footer-divider"></span>
    <ul class="footer-contact">
      <li>
        <svg viewBox="0 0 28 28" aria-hidden="true"><rect x="2" y="6" width="24" height="16" fill="none" stroke="#fff" stroke-width="2"/><path d="M2 6 l12 9 l12 -9" fill="none" stroke="#fff" stroke-width="2"/></svg>
        <span>sales@kelvarnguard.com.</span>
      </li>
      <li>
        <svg viewBox="0 0 28 28" aria-hidden="true"><g fill="none" stroke="#fff" stroke-width="2"><circle cx="14" cy="14" r="11"/><ellipse cx="14" cy="14" rx="5" ry="11"/><line x1="3" y1="14" x2="25" y2="14"/><line x1="5" y1="8" x2="23" y2="8"/><line x1="5" y1="20" x2="23" y2="20"/></g></svg>
        <span>www.kelvarnguard.com</span>
      </li>
    </ul>
  </footer>
</main>
</body>
</html>
```